Livestock Consulting Company has a logo but needs business cards and a uniform logo

My company works with farmers advising them on managing cattle and sheep. I have a logo but need business cards and a version of my logo to go onto my work shirts. I need the following wording added to my logo for my shirts "Marlowby Livestock Consulting".

```html
<!DOCTYPE html>
<html lang="en">
<head>
<meta charset="utf-8">
<title>Marlowby Livestock Consulting – Business Cards</title>
<link href="https://fonts.googleapis.com/css2?family=Roboto+Condensed:wght@400;700&family=Arimo:wght@400&display=swap" rel="stylesheet">
<style>
  :root {
    --bg: #1c1c1c;
    --brown: #6b5238;
    --brown-dark: #5d4630;
    --brown-text: #6e5234;
    --gold: #c79a62;
    --white: #ffffff;
    --ink: #3d3d3d;
  }
  * { margin: 0; padding: 0; box-sizing: border-box; }
  html, body { width: 1200px; height: 800px; overflow: hidden; }
  body {
    background: var(--bg);
    position: relative;
    font-family: "Arimo", sans-serif;
  }
  .card {
    position: absolute;
    width: 504px;
    height: 288px;
    left: 348px;
  }
  .card-front {
    top: 92px;
    background: linear-gradient(160deg, var(--brown) 0%, var(--brown-dark) 100%);
    display: flex;
    align-items: center;
    justify-content: center;
  }
  .brand {
    display: flex;
    align-items: center;
    gap: 12px;
  }
  .brand-dot {
    width: 16px; height: 16px;
    border-radius: 50%;
    background: var(--gold);
  }
  .brand-name {
    font-family: "Roboto Condensed", sans-serif;
    font-weight: 700;
    font-size: 26px;
    letter-spacing: 1px;
    text-transform: uppercase;
    color: var(--gold);
  }
  .card-back {
    top: 420px;
    background: var(--white);
  }
  .holder {
    position: absolute;
    right: 272px;
    top: 112px;
    text-align: right;
  }
  .holder-name {
    font-family: "Roboto Condensed", sans-serif;
    font-weight: 700;
    font-size: 21px;
    color: var(--brown-text);
    text-transform: uppercase;
    letter-spacing: 0.3px;
  }
  .holder-title {
    font-family: "Roboto Condensed", sans-serif;
    font-size: 12px;
    color: var(--ink);
  }
  .divider {
    position: absolute;
    left: 246px;
    top: 86px;
    width: 1px;
    height: 86px;
    background: var(--brown-text);
  }
  .contacts {
    position: absolute;
    left: 258px;
    top: 88px;
    list-style: none;
  }
  .contacts li {
    display: flex;
    align-items: center;
    gap: 6px;
    font-size: 12.5px;
    line-height: 20px;
    color: var(--ink);
  }
  .contacts svg { width: 11px; height: 11px; fill: var(--brown-text); flex: none; }
  .address-band {
    position: absolute;
    left: 0; right: 0;
    top: 196px;
    height: 24px;
    background: var(--brown);
    color: var(--white);
    font-size: 12.5px;
    display: flex;
    align-items: center;
    justify-content: center;
  }
  .base-band {
    position: absolute;
    left: 0; right: 0;
    bottom: 18px;
    height: 12px;
    background: var(--brown);
  }
</style>
</head>
<body>
  <section class="card card-front">
    <div class="brand">
      <span class="brand-dot"></span>
      <span class="brand-name">Marlowby Livestock Consulting</span>
    </div>
  </section>

  <section class="card card-back">
    <div class="holder">
      <p class="holder-name">Daniel Reyes</p>
      <p class="holder-title">President</p>
    </div>
    <div class="divider"></div>
    <ul class="contacts">
      <li><svg viewBox="0 0 12 12"><path d="M1 4c0-2 2-3 5-3s5 1 5 3v1H8V4H4v1H1z M3 6h6l1 5H2z"/></svg>555-014-2286</li>
      <li><svg viewBox="0 0 12 12"><path d="M3 0h6v12H3z M4 1v9h4V1z"/></svg>555-019-7731</li>
      <li><svg viewBox="0 0 12 12"><path d="M0 2h12v8H0z M1 3l5 4 5-4z"/></svg>info@marlowbylivestock.com</li>
      <li><svg viewBox="0 0 12 12"><circle cx="6" cy="6" r="5.5"/></svg>www.marlowbylivestock.com</li>
    </ul>
    <div class="address-band">4120 Birchwood Road, Fairbanks, Alaska 99701</div>
    <div class="base-band"></div>
  </section>
</body>
</html>
```